WinterCommuters

First, let me apologize for the short term. We just got an opportunity to place an ad in a commuter newspaper that will run throughout the winter months. We have tropical vacation rentals in Mexico, so it seems worth a shot.

We want to emphasize tropical luxury at competitive prices. Because we will be new to the audience, we need to cover a lot in one ad - images can definitely help. We are supplying photographs - feel free to crop or whatever.

We have the only private complex of luxury houses on the Mexican Caribbean coast, the "Riviera Maya" so we can accommodate anywhere from a single couple to a full wedding party. We want to show our large capacity without scaring off the single couple or small family with mom, dad, and a couple of kids.
Updates

Correction to text:  third paragraph.  The word should be "you", not "so" after "Riviera Maya,"
"As we are in the heart of the Riviera Maya, you will have "

Target Market(s)

Professionals looking to get out of the winter cold. Think tropical!

Industry/Entity Type

Wedding

Requirements
Must have
• The ad must be 5"x5" at 200 DPI (1,000 x 1000 pixels).
• The primary ad will be printed in black and white so it should be saved as a grayscale image. (I think they actually want a jpg, although a tiff would seem more logical!)
• The add will also be on the web in full color so please design the ad with color in mind and then change to grayscale after the content ends.
• Include our logo, phone number, e-mail, and website.
• Also, unless there is a good reason not to, include the four "first tier" images.
• Use the text as provided - not that some is optional.
Nice to have
• Please see the text in the attachments. OOPS: I downloaded the wrong version first - use the most recent "chicagoad" text!
• Also, unless there is a strong reason, use the "first tier" photos. We want to emphasize the accommodations, but also show large groups. We don't want to scare off the smaller groups (couples, small families) with the impression that we are only for large groups.
• The "second tier" photos are available if they would help. Both accommodation and weddings/large groups.
Should not have
• Stock photographs.
• I have (obviously) had some issues loading my files so please forgive the duplicates.

```html
<!DOCTYPE html>
<html lang="en">
<head>
<meta charset="utf-8">
<title>Laguna Villas – Winter Ad</title>
<link href="https://fonts.googleapis.com/css2?family=Arimo:wght@400&family=Tinos:ital@1&display=swap" rel="stylesheet">
<style>
  :root {
    --mint: #58f2c2;
    --blue: #3e5df2;
    --navy: #1c1f86;
    --white: #ffffff;
    --sans: "Arimo", Arial, sans-serif;
    --serif: "Tinos", "Times New Roman", serif;
  }
  html, body { margin: 0; padding: 0; overflow: hidden; background: var(--mint); }
  .ad { position: relative; width: 1200px; height: 1200px; overflow: hidden; background: var(--mint); font-family: var(--sans); }
  .backdrop { position: absolute; inset: 0; }
  .headline {
    position: absolute; right: 26px; top: 66px; width: 240px;
    color: var(--white); font-size: 34px; line-height: 1.18; text-align: right; letter-spacing: 1px;
  }
  .categories {
    position: absolute; left: 0; top: 324px; width: 1200px; height: 54px;
    display: flex; justify-content: space-around; align-items: center;
    color: var(--navy); font-size: 24px; letter-spacing: 10px;
  }
  .body-copy {
    position: absolute; left: 40px; top: 396px; width: 900px;
    color: var(--navy); font-family: var(--serif); font-style: italic;
    font-size: 23.5px; line-height: 1.22; text-align: center;
  }
  .body-copy p { margin: 0 0 22px; }
  .side-copy {
    position: absolute; right: 22px; top: 402px; width: 220px;
    color: var(--white); font-size: 23.5px; line-height: 1.42; text-align: right;
  }
  .website {
    position: absolute; left: 248px; top: 930px;
    color: var(--navy); font-size: 29px; letter-spacing: 3px;
  }
  .brand {
    position: absolute; right: 20px; top: 930px; width: 230px;
    display: flex; align-items: center; justify-content: center; gap: 10px;
    color: var(--white); font-size: 26px;
  }
  .brand-dot { width: 18px; height: 18px; border-radius: 50%; background: var(--white); }
  .contact {
    position: absolute; right: 20px; top: 1022px; width: 230px;
    color: var(--white); font-size: 26px; line-height: 1.32; text-align: center;
  }
  .tagline {
    position: absolute; left: 0; bottom: 14px; width: 1200px; text-align: center;
    color: var(--navy); font-size: 25px; letter-spacing: 4px;
  }
</style>
</head>
<body>
<div class="ad">
  <svg class="backdrop" width="1200" height="1200" viewBox="0 0 1200 1200">
    <defs>
      <linearGradient id="tropics" x1="0" y1="0" x2="0" y2="1">
        <stop offset="0" stop-color="#9fc6e8"/>
        <stop offset="0.5" stop-color="#5f8a4e"/>
        <stop offset="0.8" stop-color="#6fd0c8"/>
        <stop offset="1" stop-color="#2f8fb8"/>
      </linearGradient>
      <linearGradient id="villa" x1="0" y1="0" x2="0" y2="1">
        <stop offset="0" stop-color="#a7c4e4"/><stop offset="1" stop-color="#8a7d64"/>
      </linearGradient>
      <linearGradient id="sunset" x1="0" y1="0" x2="0" y2="1">
        <stop offset="0" stop-color="#f0b040"/><stop offset="1" stop-color="#4a3820"/>
      </linearGradient>
      <linearGradient id="ceremony" x1="0" y1="0" x2="0" y2="1">
        <stop offset="0" stop-color="#6a8a7a"/><stop offset="1" stop-color="#3f6a2a"/>
      </linearGradient>
    </defs>
    <path role="img" aria-label="Infinity pool framed by palm trees overlooking a turquoise lagoon" fill="url(#tropics)"
          d="M130 0 L960 0 L960 324 L122 324 C112 210 116 100 130 0 Z"/>
    <path class="side-panel" fill="var(--blue)"
          d="M920 0 L1200 0 L1200 1140 L862 1140 C880 1010 930 720 948 378 L948 324 C946 200 938 90 920 0 Z"/>
    <rect class="category-strip" x="0" y="324" width="1200" height="54" fill="var(--mint)"/>
    <polygon class="copy-panel" fill="var(--white)" points="48,378 949,378 946,918 26,918"/>
    <rect role="img" aria-label="Villa courtyard with tower and palm trees" x="48" y="972" width="252" height="168" fill="url(#villa)"/>
    <rect role="img" aria-label="Bride at sunset by the lagoon" x="322" y="972" width="252" height="168" fill="url(#sunset)"/>
    <rect role="img" aria-label="Outdoor wedding ceremony with guests on the lawn by the lagoon" x="592" y="972" width="252" height="168" fill="url(#ceremony)"/>
  </svg>

  <div class="headline">Wouldn't you rather be in a tropical paradise?</div>

  <div class="categories">
    <span>VACATIONS</span><span>WEDDINGS</span><span>REUNIONS</span><span>RETREATS</span>
  </div>

  <div class="body-copy">
    <p>Located in the quiet coastal village of Akumal, you get all of the best amenities, great restaurants, magnificent snorkeling and diving, beaches, and more in the laid back autmosphere that is so hard to find.</p>
    <p>As we are in the heart of the Riviera Maya, you will have access to shopping, Mayan ruins, tourist attractions, golf, sailing, diving and much more.</p>
    <p>Are you a couple looking for that perfect, secluded getaway?<br>Are you looking for a vacation in a quiet, safe, family-friendly area?<br>Do you have a family reunion, wedding, or retreat and you want everyone to be together?</p>
    <p>With 5 luxury homes to choose from, we can meet your exact needs.</p>
    <p>Visit our web site or call us directly. We look forward to hearing from you and to sharing our homes with you, your family and friends.</p>
  </div>

  <div class="side-copy">Come and relax in the only private complex of luxury houses on the beautiful Mexican Riviera Only 60 miles South of Cancun, we are a world apart from the noise and crowds of large hotels and party towns</div>

  <div class="website">www.LagunaVillasMx.com</div>

  <div class="brand"><span class="brand-dot"></span><span>Laguna Villas</span></div>

  <div class="contact">Daniel &amp; Norah<br>Pike<br>(555) 014-2738</div>

  <div class="tagline">LUXURY VILLAS AND TOWNHOUSES ON YAL-KU LAGOON, AKUMAL, MEXICO</div>
</div>
</body>
</html>
```